Need a Menu with our Logo and price and food items

Need to develop a Menu page that attracts our customers with our logo we have a basic logo and is very poor I can attach our logo and menu Please help us. The Restaurant menu is attached it must be two pages.must include a little of our history which I will provide very soon.

Industry/Entity Type

Restaurant

Font styles to use
Sans Serif

Requirements
Must have
• Casa Benvidal
1837 Calle Orvena
Punta Los Cedrales
San Juan, PR 000912
tel (787) 513-4072
email: casabenvidalpr@fondamail.com
Nice to have
• a google map for directions

```html
<!DOCTYPE html>
<html lang="es">
<head>
<meta charset="utf-8">
<title>Casa Benvidal — Menú</title>
<link rel="stylesheet" href="https://fonts.googleapis.com/css2?family=Hind:wght@500;600;700&family=Pinyon+Script&display=swap">
<style>
  :root{
    --bg:#e7e3de;
    --paper:#fdfdfb;
    --ink:#1f1f1f;
    --script:#a8c2df;
    --brand:#5a9ea3;
    --note:#a9c1dc;
    --photo-frame:#ffffff;
  }
  *{margin:0;padding:0;box-sizing:border-box}
  html,body{width:1200px;height:992px;overflow:hidden;background:var(--bg)}
  body{position:relative;font-family:"Hind",Arial,sans-serif;color:var(--ink)}
  .page{position:absolute;background:var(--paper);box-shadow:0 1px 3px rgba(0,0,0,.15)}
  .page--left{left:40px;top:137px;width:560px;height:728px}
  .page--right{left:605px;top:137px;width:563px;height:711px}
  .brand{position:absolute;font-family:"Hind",Arial,sans-serif;font-weight:600;font-size:15px;color:var(--brand);letter-spacing:.3px;display:flex;align-items:center;gap:5px}
  .brand::before{content:"";width:8px;height:8px;border-radius:50%;background:var(--brand)}
  .section-title{position:absolute;font-family:"Pinyon Script",cursive;color:var(--script);font-size:42px;line-height:1;white-space:nowrap;transform:translateX(-50%)}
  .menu-col{position:absolute;font-size:10.5px;font-weight:600;line-height:14.6px}
  .item{display:flex;align-items:baseline;white-space:nowrap}
  .item .dots{flex:1;border-bottom:2px dotted var(--ink);margin:0 2px 3px;min-width:6px}
  .item--indent{padding-left:14px;font-style:italic}
  .label{margin-top:2px}
  .gap{height:4px}
  .photo{position:absolute;background:var(--photo-frame);padding:8px 8px 26px;box-shadow:0 2px 6px rgba(0,0,0,.3)}
  .photo .shot{width:100%;height:100%;border-radius:8px}
  .photo .caption{position:absolute;bottom:3px;left:0;right:0;text-align:center;font-family:"Pinyon Script",cursive;color:var(--script);font-size:15px}
  .sides{position:absolute;font-size:10.5px;font-weight:600;line-height:13.8px}
  .sides em{font-style:italic}
  .allergy{position:absolute;left:0;right:0;top:689px;text-align:center;font-weight:700;font-style:italic;font-size:11.5px;color:var(--note);letter-spacing:.2px}
</style>
</head>
<body>

<section class="page page--left">
  <div class="brand" style="left:12px;top:20px">Casa Benvidal</div>

  <h2 class="section-title" style="left:285px;top:40px">Sopas y Aperitivos</h2>
  <div class="menu-col" style="left:63px;top:89px;width:203px">
    <div class="item"><span>Crema del día</span><span class="dots"></span><span>$4</span></div>
    <div class="gap"></div>
    <div class="label">Surtido de la Montaña</div>
    <div class="item item--indent"><span>4 personas</span><span class="dots"></span><span>$ 23</span></div>
    <div class="item item--indent"><span>2 personas</span><span class="dots"></span><span>14</span></div>
    <div class="gap"></div>
    <div class="item"><span>Camarones al Ajillo</span><span class="dots"></span><span>12</span></div>
    <div class="item"><span>Sepia al Ajillo</span><span class="dots"></span><span>12</span></div>
    <div class="item"><span>Boquerones fritos</span><span class="dots"></span><span>3</span></div>
    <div class="item"><span>Chorizo al Vino</span><span class="dots"></span><span>10</span></div>
    <div class="item"><span>Empanadillas de Carne (4)</span><span class="dots"></span><span>7</span></div>
    <div class="item"><span>Empanadillas de Carrucho (4)</span><span class="dots"></span><span>10</span></div>
    <div class="item"><span>Empanadillas de Langosta (4)</span><span class="dots"></span><span>10</span></div>
    <div class="item"><span>Empanadillas de Jueyes (4)</span><span class="dots"></span><span>10</span></div>
  </div>
  <div class="menu-col" style="left:298px;top:89px;width:203px">
    <div class="item"><span>Longanizas de Pollo (de Orocovis)</span><span class="dots"></span><span>7</span></div>
    <div class="item"><span>Longanizas de Cerdo (de Orocovis)</span><span class="dots"></span><span>7</span></div>
    <div class="item"><span>Longanizas de Pavochón (de Orocovis)</span><span class="dots"></span><span>7</span></div>
    <div class="item"><span>Longanizas de Chorizo</span><span class="dots"></span><span>7</span></div>
    <div class="item"><span>Carne de Cerdo ahumada de Naranjito</span><span class="dots"></span><span>3</span></div>
    <div class="item"><span>Croquetas de Jamón (4)</span><span class="dots"></span><span>6</span></div>
    <div class="item"><span>Pimientos del Piquillo rellenos de Cangrejo</span><span class="dots"></span><span>13</span></div>
    <div class="item"><span>Calamares a la Romana</span><span class="dots"></span><span>10</span></div>
    <div class="item"><span>Buñuelos de Bacalao</span><span class="dots"></span><span>10</span></div>
    <div class="item"><span>Sorullitos de Maíz</span><span class="dots"></span><span>7</span></div>
    <div class="item"><span>Bandeja de Manchego y Prosciutto</span><span class="dots"></span><span>13</span></div>
    <div class="item"><span>Morcilla de Aguas Buenas</span><span class="dots"></span><span>8</span></div>
    <div class="item"><span>Mejillones rellenos (6)</span><span class="dots"></span><span>12</span></div>
  </div>

  <h2 class="section-title" style="left:275px;top:305px">Ensaladas</h2>
  <div class="menu-col" style="left:63px;top:347px;width:203px">
    <div class="item"><span>Ensalada Griega</span><span class="dots"></span><span>$ 8</span></div>
    <div class="item"><span>Ensalada Griega con Pollo</span><span class="dots"></span><span>13</span></div>
    <div class="item"><span>Ensalada Griega con Camarones</span><span class="dots"></span><span>18</span></div>
  </div>
  <div class="menu-col" style="left:298px;top:347px;width:203px">
    <div class="item"><span>Ensalada César</span><span class="dots"></span><span>8</span></div>
    <div class="item"><span>Ensalada César con Pollo</span><span class="dots"></span><span>11</span></div>
    <div class="item"><span>Ensalada César con Camarones</span><span class="dots"></span><span>18</span></div>
  </div>

  <h2 class="section-title" style="left:275px;top:428px">Carnes</h2>
  <div class="menu-col" style="left:63px;top:471px;width:339px;line-height:15.2px">
    <div class="item"><span>Ossobuco</span><span class="dots"></span><span>$ 30</span></div>
    <div class="item"><span>Churrasco</span><span class="dots"></span><span>18</span></div>
    <div class="item"><span>Biftec Encebollado</span><span class="dots"></span><span>10</span></div>
    <div class="item"><span>Chuletas Fritas</span><span class="dots"></span><span>11</span></div>
    <div class="item"><span>Chuletas Can Can</span><span class="dots"></span><span>16</span></div>
    <div class="item"><span>Pechugas de Pollo a la Francesca</span><span class="dots"></span><span>15</span></div>
    <div class="item"><span>Pechugas de Pollo rellenas de Prosciutto</span><span class="dots"></span><span>18</span></div>
    <div class="item"><span>Pechugas de Pollo rellenas de Camarones</span><span class="dots"></span><span>20</span></div>
    <div class="item"><span>Milanesa de Res</span><span class="dots"></span><span>15</span></div>
    <div class="item"><span>Milanesa de Pollo</span><span class="dots"></span><span>15</span></div>
    <div class="item"><span>Empanada de Res</span><span class="dots"></span><span>15</span></div>
    <div class="item"><span>Empanada de Pollo</span><span class="dots"></span><span>15</span></div>
    <div class="item"><span>Carne Frita Encebollada</span><span class="dots"></span><span>13</span></div>
    <div class="item"><span>New York Steak</span><span class="dots"></span><span>26</span></div>
    <div class="item"><span>Pasteles (Masa Cerdo, Yuca Cerdo)</span><span class="dots"></span><span>7 c/u</span></div>
    <div class="item"><span>Otro Plato Aqui</span><span class="dots"></span><span>27</span></div>
  </div>

  <figure class="photo" style="left:417px;top:432px;width:130px;height:128px;transform:rotate(-2deg)">
    <div class="shot" role="img" aria-label="Foto del filete especial con salsa en plato blanco" style="background:radial-gradient(circle at 50% 55%,#7a3a22 0,#5a2a18 30%,#d9d4cc 60%,#e9e6e1 100%)"></div>
    <figcaption class="caption">Filete especial</figcaption>
  </figure>
  <figure class="photo" style="left:430px;top:573px;width:130px;height:135px;transform:rotate(3deg)">
    <div class="shot" role="img" aria-label="Foto del filete a los 4 pimientos con papas" style="background:radial-gradient(circle at 45% 60%,#5c2414 0,#3e1a10 30%,#b8a89a 62%,#ddd6ce 100%)"></div>
    <figcaption class="caption">Filete a los 4 pimientos</figcaption>
  </figure>
</section>

<section class="page page--right">
  <div class="brand" style="left:440px;top:30px">Casa Benvidal</div>

  <h2 class="section-title" style="left:270px;top:45px">Pescados y Mariscos</h2>
  <div class="menu-col" style="left:62px;top:89px;width:203px;line-height:13.6px">
    <div class="item"><span>Langostinos a la plancha</span><span class="dots"></span><span>$ 24</span></div>
    <div class="item"><span>Langosta al Mojo Isleño</span><span class="dots"></span><span>29</span></div>
    <div class="item"><span>Langosta a la Mantequilla</span><span class="dots"></span><span>29</span></div>
    <div class="item"><span>Mero en Salsa con Alcaparras</span><span class="dots"></span><span>23</span></div>
    <div class="item"><span>Mero al Mojo Isleño</span><span class="dots"></span><span>23</span></div>
    <div class="item"><span>Dorado al Ajillo con Almendras</span><span class="dots"></span><span>22</span></div>
    <div class="item"><span>Asopao de Langosta</span><span class="dots"></span><span>29</span></div>
    <div class="item"><span>Asopao de Camarones</span><span class="dots"></span><span>22</span></div>
    <div class="item"><span>Camarones al Ajillo</span><span class="dots"></span><span>22</span></div>
    <div class="item"><span>Casuela de Bacalao</span><span class="dots"></span><span>24</span></div>
    <div class="item"><span>Rodaballo en Salsa con Alcaparras</span><span class="dots"></span><span>29</span></div>
    <div class="item"><span>Salmón en Salsa de Miel y Mostaza</span><span class="dots"></span><span>22</span></div>
  </div>
  <div class="menu-col" style="left:297px;top:89px;width:203px;line-height:13.6px">
    <div class="item"><span>Mofongo relleno de Langosta</span><span class="dots"></span><span>29</span></div>
    <div class="item"><span>Mofongo relleno de Camarones</span><span class="dots"></span><span>24</span></div>
    <div class="item"><span>Bacalao al Pil Pil</span><span class="dots"></span><span>29</span></div>
  </div>

  <figure class="photo" style="left:290px;top:141px;width:125px;height:125px;transform:rotate(-1deg)">
    <div class="shot" role="img" aria-label="Foto de bacalao a la riojana con pimientos" style="background:radial-gradient(circle at 50% 55%,#c5d9b0 0,#8aa86a 22%,#d8dcd0 55%,#eef0ea 100%)"></div>
    <figcaption class="caption">Bacalao Riojana</figcaption>
  </figure>
  <figure class="photo" style="left:422px;top:143px;width:138px;height:130px;transform:rotate(4deg)">
    <div class="shot" role="img" aria-label="Foto de langostinos a la plancha con papas" style="background:radial-gradient(circle at 50% 45%,#d6612a 0,#b8481c 30%,#6a4a36 65%,#3a2a20 100%)"></div>
    <figcaption class="caption">Langostinos</figcaption>
  </figure>

  <h2 class="section-title" style="left:270px;top:283px">Arroces</h2>
  <div class="menu-col" style="left:62px;top:322px;width:203px">
    <div class="item"><span>Risotto de Churrasco</span><span class="dots"></span><span>$ 18</span></div>
    <div class="item"><span>Risotto de Prosciutto</span><span class="dots"></span><span>18</span></div>
    <div class="item"><span>Risotto de Setas</span><span class="dots"></span><span>15</span></div>
    <div class="item"><span>Risotto de Langosta</span><span class="dots"></span><span>29</span></div>
    <div class="item"><span>Risotto de Camarones</span><span class="dots"></span><span>23</span></div>
    <div class="item"><span>Risotto de Pollo</span><span class="dots"></span><span>15</span></div>
  </div>
  <div class="menu-col" style="left:297px;top:322px;width:203px">
    <div class="item"><span>Risotto de Sepia</span><span class="dots"></span><span>20</span></div>
    <div class="item"><span>Risotto de Gandules</span><span class="dots"></span><span>15</span></div>
    <div>Risotto de Gandules con Carne de Cerdo</div>
    <div class="item"><span>ahumada e Longaniza</span><span class="dots"></span><span>18</span></div>
    <div class="item"><span>Risotto con Ajo, Nueces y Albahaca</span><span class="dots"></span><span>10</span></div>
    <div class="item"><span>Asopao de Gandules con Masitas de Cerdo</span><span class="dots"></span><span>X</span></div>
  </div>

  <h2 class="section-title" style="left:270px;top:432px">Pastas</h2>
  <div class="menu-col" style="left:62px;top:476px;width:203px">
    <div class="item"><span>Fetuchini con Camarones en Salsa Rosada</span><span class="dots"></span><span>$X</span></div>
    <div class="item"><span>Fetuchini con Camarones en Salsa Alfredo</span><span class="dots"></span><span>X</span></div>
  </div>
  <div class="menu-col" style="left:297px;top:476px;width:203px">
    <div class="item"><span>Fetuchini con Pollo en Salsa Rosada</span><span class="dots"></span><span>X</span></div>
    <div class="item"><span>Fetuchini con Pollo en Salsa Rosada</span><span class="dots"></span><span>X</span></div>
  </div>

  <h2 class="section-title" style="left:155px;top:532px">Acompañantes</h2>
  <div class="sides" style="left:62px;top:576px;width:203px">
    <em>Tostones de Plátano / Tostones de Pana / Amarillos / Papas del día / Arroz Blanco y Habichuelas Coloradas / Arroz Mamposteao / Ensalada / Vegetales</em>
    <div>Un acompanante por plato. Si desea uno</div>
    <div class="item"><span>extra</span><span class="dots"></span><span>$ 4 c/u</span></div>
    <div class="item"><span>Mofongo</span><span class="dots"></span><span>$ X</span></div>
  </div>

  <h2 class="section-title" style="left:380px;top:532px">Postres</h2>
  <div class="sides" style="left:297px;top:576px;width:203px">
    <div>Tres Leches / Flan de Coco / Helado de Queso / Helado de Maíz / Helado de</div>
    <div class="item"><span>Chocolate y Pie de Limón</span><span class="dots"></span><span>$ X c/u</span></div>
    <div class="item" style="margin-top:2px"><span>Café Espresso</span><span class="dots"></span><span>$ X</span></div>
    <div class="item" style="margin-top:2px"><span>Té (Verde, Negro é Manzanilla)</span><span class="dots"></span><span>$ X</span></div>
  </div>

  <p class="allergy">SI ES ALÉRGICO A ALGÚN ALIMENTO, FAVOR NOTIFICÁRSELO AL MESERO.</p>
</section>

</body>
</html>
```